We are looking to create a graphic that will be used in Facebook posts each week to show the daily Porchlight Report. Attached is an example of what we are looking for. We need to be able to update the forecast. So we will need hi-res vector files. The graphics need to represent the level of mosquito activity: SLIGHT, AVERAGE, INTENSE, EXTREME

```html
<!DOCTYPE html>
<html lang="en">
<head>
<meta charset="utf-8">
<title>Porchlight Report</title>
<link rel="stylesheet" href="https://fonts.googleapis.com/css2?family=Bebas+Neue&family=Montserrat:wght@900&display=swap">
<style>
  :root {
    --ink: #1f1a1f;
    --white: #ffffff;
    --card-border: #d9d9d9;
    --grass-dark: #2f6a12;
    --grass-mid: #5aa81c;
    --grass-light: #9fd84a;
    --body-amber: #d89a3a;
    --icon-red: #7a1212;
    --g-green: #36ee1a;
    --g-lime: #b8ea1c;
    --g-yellow: #ffe100;
    --g-orange: #ff8a00;
    --g-red: #e40000;
    --g-maroon: #960000;
    --g-dark: #520000;
  }
  * { margin: 0; padding: 0; box-sizing: border-box; }
  html, body { width: 1200px; height: 677px; overflow: hidden; background: var(--grass-mid); }
  .poster { position: relative; width: 1200px; height: 677px; overflow: hidden; }
  .backdrop {
    position: absolute; inset: 0;
    background:
      radial-gradient(ellipse 38% 30% at 58% 18%, rgba(216,154,58,0.85), rgba(216,154,58,0) 70%),
      radial-gradient(ellipse 60% 50% at 50% 85%, var(--grass-light), rgba(159,216,74,0) 70%),
      linear-gradient(180deg, var(--grass-dark) 0%, var(--grass-mid) 45%, var(--grass-dark) 100%);
  }
  .headline { position: absolute; left: 58px; top: 132px; width: 1090px; height: 100px; }
  .headline text {
    font-family: 'Montserrat', sans-serif; font-weight: 900; font-size: 98px;
    fill: var(--white); stroke: var(--ink); stroke-width: 14px; stroke-linejoin: round;
    paint-order: stroke fill;
  }
  .week { position: absolute; left: 53px; top: 262px; display: flex; gap: 18px; }
  .day-card {
    width: 141px; height: 223px; background: var(--white);
    border: 1px solid var(--card-border); border-radius: 4px;
    position: relative; text-align: center;
    font-family: 'Bebas Neue', sans-serif; color: var(--ink);
  }
  .day-name { position: absolute; top: 10px; left: 0; right: 0; font-size: 29px; line-height: 1; }
  .day-date { position: absolute; top: 41px; left: 0; right: 0; font-size: 29px; line-height: 1; }
  .gauge { position: absolute; left: 16px; top: 74px; width: 108px; height: 108px; }
  .gauge-arc {
    position: absolute; inset: 0; border-radius: 50%;
    background: conic-gradient(from 225deg,
      var(--g-green) 0%, var(--g-lime) 14%, var(--g-yellow) 28%,
      var(--g-orange) 40%, var(--g-red) 50%, var(--g-maroon) 62%,
      var(--g-dark) 75%, transparent 75%);
    -webkit-mask: radial-gradient(circle, transparent 37px, #000 38px);
    mask: radial-gradient(circle, transparent 37px, #000 38px);
  }
  .gauge-icon {
    position: absolute; left: 38px; top: 38px; width: 32px; height: 32px;
    border-radius: 50%; background: var(--icon-red);
  }
  .level { position: absolute; top: 186px; left: 0; right: 0; font-size: 26px; line-height: 1; }
</style>
</head>
<body>
<main class="poster">
  <div class="backdrop" role="img" aria-label="Close-up of a mosquito resting in green grass"></div>

  <svg class="headline" viewBox="0 0 1090 100" aria-label="Porchlight Report">
    <text x="8" y="86" textLength="1074" lengthAdjust="spacingAndGlyphs">PORCHLIGHT REPORT</text>
  </svg>

  <section class="week">
    <article class="day-card"><div class="day-name">THU</div><div class="day-date">7/21</div>
      <div class="gauge"><div class="gauge-arc"></div><div class="gauge-icon" role="img" aria-label="Mosquito icon"></div></div>
      <div class="level">SLIGHT</div></article>
    <article class="day-card"><div class="day-name">FRI</div><div class="day-date">7/22</div>
      <div class="gauge"><div class="gauge-arc"></div><div class="gauge-icon" role="img" aria-label="Mosquito icon"></div></div>
      <div class="level">AVERAGE</div></article>
    <article class="day-card"><div class="day-name">SAN</div><div class="day-date">7/24</div>
      <div class="gauge"><div class="gauge-arc"></div><div class="gauge-icon" role="img" aria-label="Mosquito icon"></div></div>
      <div class="level">INTENSE</div></article>
    <article class="day-card"><div class="day-name">SUN</div><div class="day-date">7/25</div>
      <div class="gauge"><div class="gauge-arc"></div><div class="gauge-icon" role="img" aria-label="Mosquito icon"></div></div>
      <div class="level">EXTREME</div></article>
    <article class="day-card"><div class="day-name">MON</div><div class="day-date">7/26</div>
      <div class="gauge"><div class="gauge-arc"></div><div class="gauge-icon" role="img" aria-label="Mosquito icon"></div></div>
      <div class="level">AVERAGE</div></article>
    <article class="day-card"><div class="day-name">TUE</div><div class="day-date">7/27</div>
      <div class="gauge"><div class="gauge-arc"></div><div class="gauge-icon" role="img" aria-label="Mosquito icon"></div></div>
      <div class="level">INTENSE</div></article>
    <article class="day-card"><div class="day-name">WED</div><div class="day-date">7/28</div>
      <div class="gauge"><div class="gauge-arc"></div><div class="gauge-icon" role="img" aria-label="Mosquito icon"></div></div>
      <div class="level">SLIGHT</div></article>
  </section>
</main>
</body>
</html>
```